Online medical reviews website needs banner advert!

We need banner advert templates for our website, www.traineepanel.net. These should meet the technical requirements of our partner (uploaded).

Our groundbreaking website allows doctors in training to rate and review their training.

The adverts should use the same modern design language and colour scheme as our website. They should use the text 'Help a junior doctor make a big decision - rate your training!'.

Vector assets should be supplied, allowing us to use alternative text in future.
Updates

Industry/Entity Type

Healthcare

Font styles to use
Other font styles liked:
• Karla

Colors
3277b5
0555a3
ffffff

Requirements
Must have
• Similar design to our website. Should be elegant & modern. Must allow future text to be easily inserted.
Should not have
• Unrelated design.

```html
<!DOCTYPE html>
<html lang="en">
<head>
<meta charset="utf-8">
<title>Trainee Panel – Banner</title>
<link href="https://fonts.googleapis.com/css2?family=Karla:wght@500;700;800&display=swap" rel="stylesheet">
<style>
  :root {
    --navy: #102f6c;
    --brand-blue: #0555a3;
    --sky: #3277b5;
    --band: #0a3f85;
    --white: #ffffff;
    --bg-top: #eef4fa;
    --bg-mid: #e3edf6;
    --bg-soft: #d5e4f1;
  }
  html, body {
    margin: 0;
    padding: 0;
    overflow: hidden;
    background: var(--white);
  }
  .banner {
    position: relative;
    width: 1200px;
    height: 451px;
    overflow: hidden;
    font-family: "Karla", Arial, sans-serif;
    background: linear-gradient(100deg, var(--bg-top) 0%, var(--white) 35%, var(--bg-mid) 70%, var(--bg-soft) 100%);
  }
  .visual {
    position: absolute;
  }
  .visual--map {
    left: 465px;
    top: 0;
    width: 330px;
    height: 370px;
    background: radial-gradient(ellipse at 50% 45%, rgba(120, 165, 210, 0.35) 0%, rgba(120, 165, 210, 0.12) 55%, rgba(255, 255, 255, 0) 75%);
  }
  .visual--capsules {
    right: 0;
    top: 0;
    width: 400px;
    height: 330px;
    background: radial-gradient(ellipse at 60% 40%, rgba(80, 180, 235, 0.45) 0%, rgba(170, 190, 210, 0.35) 45%, rgba(255, 255, 255, 0) 75%);
  }
  .visual--lab-tubes {
    left: 0;
    bottom: 0;
    width: 470px;
    height: 260px;
    background: radial-gradient(ellipse at 35% 75%, rgba(150, 175, 200, 0.55) 0%, rgba(200, 215, 230, 0.4) 50%, rgba(255, 255, 255, 0) 78%);
  }
  .brand {
    position: absolute;
    left: 54px;
    top: 22px;
    display: flex;
    align-items: center;
    gap: 7px;
    color: var(--brand-blue);
    font-weight: 700;
    font-size: 19px;
    letter-spacing: -0.2px;
  }
  .brand__mark {
    width: 9px;
    height: 9px;
    background: var(--sky);
  }
  .headline {
    position: absolute;
    left: 54px;
    top: 96px;
    margin: 0;
    width: 620px;
    color: var(--navy);
    font-weight: 800;
    font-size: 41px;
    line-height: 1.22;
    letter-spacing: 0.3px;
  }
  .cta {
    position: absolute;
    left: 56px;
    top: 258px;
    width: 254px;
    height: 40px;
    display: flex;
    align-items: center;
    justify-content: center;
    background: var(--navy);
    color: var(--white);
    font-weight: 700;
    font-size: 16px;
    letter-spacing: 0.3px;
  }
  .url-band {
    position: absolute;
    right: 0;
    bottom: 0;
    width: 390px;
    height: 46px;
  }
  .url-band svg {
    position: absolute;
    inset: 0;
  }
  .url-band__text {
    position: absolute;
    right: 24px;
    top: 0;
    height: 46px;
    display: flex;
    align-items: center;
    color: var(--white);
    font-weight: 700;
    font-size: 18px;
    letter-spacing: 3px;
  }
</style>
</head>
<body>
<div class="banner">
  <div class="visual visual--map" role="img" aria-label="Dotted world map showing Asia and Australia"></div>
  <div class="visual visual--capsules" role="img" aria-label="Blue and grey medicine capsules spilling from a bottle"></div>
  <div class="visual visual--lab-tubes" role="img" aria-label="Glass test tubes with a laboratory pipette"></div>

  <div class="brand">
    <span>Trainee Panel</span>
    <span class="brand__mark"></span>
  </div>

  <h1 class="headline">Help a junior doctor make a big decision</h1>

  <div class="cta">Rate &amp; revies your training</div>

  <div class="url-band">
    <svg width="390" height="46" viewBox="0 0 390 46" aria-hidden="true">
      <polygon points="22,0 390,0 390,46 0,46" fill="var(--band)"/>
    </svg>
    <span class="url-band__text">www.traineepanel.net</span>
  </div>
</div>
</body>
</html>
```